profestional carpet and furniture cleaning service

I have a Varnel cruza 2018 that I would like to wrap the sides the back and the back I'll send you pictures of my van, and some other pictures that could be utilized on the wrap ,it's a carpet and furniture cleaning company.
And probably I will Need some business cards design as well
The name of the company is lantern, I am getting a new phone number for this company so for now I cannot provide you the number but I will get it shortly
I live in Montreal Canada and all the texts has to be in French.
the text that should show on the wrap is.
Nettoyage à la vapeur
Tapis
Meuble
Matelas
Céramique
Conduis de ventilation
and the phone number ...

Target Market(s)

residential

Industry/Entity Type

cleaning

Font styles to use
Sans Serif

Colors
0054AA
0677BA
7BADD7
CADEEF
E8F1F8
59FF00
82FF00
B8FF75
E3FFCB
F4FFEA
F0912C
F2A743
F7CA91
FBE8D2
FDF5EE
EB3D1F
EC4F4E
F09395
F8D3D4
FCEDEE

Requirements
Nice to have
• some pictures and add some steam vapor picture in the back round

```html
<!DOCTYPE html>
<html lang="fr">
<head>
<meta charset="utf-8">
<title>lantern – habillage Varnel cruza</title>
<link rel="stylesheet" href="https://fonts.googleapis.com/css2?family=Oswald:wght@500;700&family=Archivo+Black&display=swap">
<style>
  :root{
    --page:#eef0f2;
    --wrap-black:#050505;
    --band-black:#000000;
    --blue-deep:#1d2f9e;
    --blue-mid:#2f4fd0;
    --blue-brand:#0054AA;
    --blue-sky:#0677BA;
    --blue-light:#7BADD7;
    --blue-pale:#CADEEF;
    --white:#ffffff;
    --photo-grey:#9a9a9a;
    --photo-light:#d8d8d8;
  }
  html,body{margin:0;padding:0;}
  body{width:1200px;height:2605px;overflow:hidden;background:var(--page);}
  .wrap-sheet{display:block;width:1200px;height:2605px;}
  .phone-label{font-family:"Oswald",sans-serif;font-weight:500;fill:var(--white);}
  .phone-number{font-family:"Oswald",sans-serif;font-weight:700;fill:var(--white);}
  .service-item{font-family:"Archivo Black",sans-serif;font-size:9px;fill:var(--white);}
  .brand-name{font-family:"Oswald",sans-serif;font-weight:700;fill:var(--blue-mid);}
</style>
</head>
<body>
<svg class="wrap-sheet" viewBox="0 0 1200 2605" xmlns="http://www.w3.org/2000/svg">
  <defs>
    <linearGradient id="photoTone" x1="0" y1="0" x2="1" y2="1">
      <stop offset="0" stop-color="var(--photo-light)"/>
      <stop offset="1" stop-color="var(--photo-grey)"/>
    </linearGradient>
    <linearGradient id="productTone" x1="0" y1="0" x2="0" y2="1">
      <stop offset="0" stop-color="#e9e9ee"/>
      <stop offset="1" stop-color="#b9bcc8"/>
    </linearGradient>
    <symbol id="tick" viewBox="0 0 10 10">
      <circle cx="5" cy="5" r="4.2" fill="none" stroke="#fff" stroke-width="1.2"/>
      <path d="M3 5.2 L4.5 6.7 L7.2 3.6" fill="none" stroke="#fff" stroke-width="1.3"/>
    </symbol>
    <symbol id="phoneIcon" viewBox="0 0 20 20">
      <circle cx="10" cy="10" r="9" fill="#fff"/>
      <path d="M6.5 5.5 l2 -0.5 l1 2.5 l-1.2 1 a6 6 0 0 0 3 3 l1 -1.2 l2.5 1 l-0.5 2 a8 8 0 0 1 -7.8 -7.8z" fill="#000"/>
    </symbol>
  </defs>

  <!-- Passenger side -->
  <g class="side-panel side-right">
    <path d="M100 150 H760 Q800 150 830 175 L1000 290 Q1130 320 1130 350 V470 H100 Z" fill="var(--wrap-black)"/>
    <rect x="100" y="395" width="1030" height="40" fill="var(--band-black)"/>
    <path d="M580 150 H640 Q560 280 650 460 H595 Q510 290 580 150 Z" fill="var(--blue-deep)"/>
    <path d="M610 150 H670 Q590 280 690 460 H650 Q560 280 610 150 Z" fill="var(--blue-light)" opacity=".85"/>
    <path d="M635 150 H690 Q620 280 700 460 H690 Q595 280 635 150 Z" fill="var(--blue-sky)"/>
    <rect x="100" y="152" width="150" height="160" fill="url(#photoTone)" role="img" aria-label="Photo d'équipement de nettoyage à la vapeur"/>
    <circle cx="287" cy="215" r="38" fill="url(#photoTone)" stroke="#cfcfcf" stroke-width="3" role="img" aria-label="Photo de nettoyage de tapis"/>
    <circle cx="268" cy="295" r="56" fill="url(#photoTone)" stroke="#cfcfcf" stroke-width="3" role="img" aria-label="Photo d'une buse d'extraction sur un tapis"/>
    <text class="brand-name" x="440" y="295" font-size="52" text-anchor="middle">lantern</text>
    <use href="#phoneIcon" x="484" y="371" width="16" height="16"/>
    <text class="phone-label" x="505" y="385" font-size="15">Call Us:</text>
    <text class="phone-number" x="484" y="430" font-size="48">000 111 222</text>
    <g class="service-list">
      <use href="#tick" x="772" y="321" width="9" height="9"/><text class="service-item" x="784" y="329">Tapis</text>
      <use href="#tick" x="772" y="339" width="9" height="9"/><text class="service-item" x="784" y="347">Meuble</text>
      <use href="#tick" x="772" y="357" width="9" height="9"/><text class="service-item" x="784" y="365">Matelas</text>
      <use href="#tick" x="832" y="321" width="9" height="9"/><text class="service-item" x="844" y="329">Céramique</text>
      <use href="#tick" x="832" y="339" width="9" height="9"/><text class="service-item" x="844" y="347">Nettoyage à la vapeur</text>
      <use href="#tick" x="832" y="357" width="9" height="9"/><text class="service-item" x="844" y="365">Conduis de ventilation</text>
    </g>
  </g>

  <!-- Driver side -->
  <g class="side-panel side-left">
    <path d="M1065 1015 H400 Q365 1015 330 1040 L170 1150 Q40 1180 30 1210 V1330 H1065 Z" fill="var(--wrap-black)"/>
    <rect x="30" y="1253" width="1035" height="45" fill="var(--band-black)"/>
    <path d="M485 1015 H545 Q610 1150 530 1320 H478 Q560 1150 485 1015 Z" fill="var(--blue-deep)"/>
    <path d="M510 1015 H570 Q640 1150 560 1320 H520 Q600 1150 510 1015 Z" fill="var(--blue-light)" opacity=".85"/>
    <path d="M540 1015 H590 Q650 1150 580 1320 H560 Q630 1150 540 1015 Z" fill="var(--blue-sky)"/>
    <path d="M930 1020 H1058 V1185 Q990 1190 950 1160 Z" fill="url(#photoTone)" role="img" aria-label="Photo d'une buse d'extraction sur un tapis"/>
    <circle cx="870" cy="1082" r="35" fill="url(#photoTone)" stroke="#cfcfcf" stroke-width="3" role="img" aria-label="Photo de nettoyage de tapis"/>
    <circle cx="887" cy="1168" r="55" fill="url(#photoTone)" stroke="#cfcfcf" stroke-width="3" role="img" aria-label="Photo d'équipement de nettoyage à la vapeur"/>
    <text class="brand-name" x="700" y="1160" font-size="52" text-anchor="middle">lantern</text>
    <use href="#phoneIcon" x="572" y="1236" width="16" height="16"/>
    <text class="phone-label" x="593" y="1250" font-size="15">Call Us:</text>
    <text class="phone-number" x="572" y="1295" font-size="48">000 111 222</text>
    <g class="service-list">
      <use href="#tick" x="200" y="1190" width="9" height="9"/><text class="service-item" x="212" y="1198">Tapis</text>
      <use href="#tick" x="200" y="1206" width="9" height="9"/><text class="service-item" x="212" y="1214">Meuble</text>
      <use href="#tick" x="200" y="1222" width="9" height="9"/><text class="service-item" x="212" y="1230">Matelas</text>
      <use href="#tick" x="260" y="1190" width="9" height="9"/><text class="service-item" x="272" y="1198">Céramique</text>
      <use href="#tick" x="260" y="1206" width="9" height="9"/><text class="service-item" x="272" y="1214">Nettoyage à la vapeur</text>
      <use href="#tick" x="260" y="1222" width="9" height="9"/><text class="service-item" x="272" y="1230">Conduis de ventilation</text>
    </g>
  </g>

  <!-- Rear doors -->
  <g class="rear-panel">
    <path d="M300 1800 H880 Q915 1800 915 1835 V2265 H255 V1835 Q255 1800 300 1800 Z" fill="var(--wrap-black)"/>
    <line x1="575" y1="1800" x2="575" y2="2265" stroke="#1a1a1a" stroke-width="2"/>
    <path d="M300 1820 H860 Q875 1820 872 1840 L865 2035 Q860 2045 845 2045 H310 Q290 2045 288 2030 L283 1840 Q283 1820 300 1820 Z" fill="url(#productTone)" role="img" aria-label="Photo de la gamme de produits nettoyants en bidons"/>
    <text class="brand-name" x="410" y="2175" font-size="56" text-anchor="middle">lantern</text>
    <use href="#phoneIcon" x="592" y="2134" width="24" height="24"/>
    <text class="phone-label" x="622" y="2156" font-size="22">Call Us:</text>
    <text class="phone-number" x="592" y="2222" font-size="66">000 111 222</text>
  </g>
</svg>
</body>
</html>
```